Yard sign design for high end luxury home builder.

Need a design for signage on custom homes that are being built. I already have a logo that I am satisfied with that needs to be incorporated. I need the following incorporated in the design of the sign-
- Lic number 318562
- phone number (555) 271-4038
- pendrickhomeworks.com
- Logo/Branding

If possible it may be nice to have the following quote that is on are business cards-

Quote from Osmund of Veltarra-
HE WHO WORKS WITH HIS HANDS IS A LABORER.
HE WHO WORKS WITH HIS HANDS & HIS HEAD IS A CRAFTSMAN.
HE WHO WORKS WITH HIS HANDS & HIS HEAD & HIS HEART IS AN ARTISAN.
-OSMUND OF VELTARRA

Target Market(s)

Archetect, Designers, Clients desiring to build a new home or remodel.

Colors
fde9d4
fee4d5
fabb94
fac994
faa54b
f68d4d
f37122
f78f20
f68e4e

Requirements
Must have
• - Lic number 318562
• - phone number (555) 271-4038
• - pendrickhomeworks.com
• - Logo/Branding
Nice to have
• Quote from Osmund of Veltarra-
• HE WHO WORKS WITH HIS HANDS IS A LABORER.
• HE WHO WORKS WITH HIS HANDS & HIS HEAD IS A CRAFTSMAN.
• HE WHO WORKS WITH HIS HANDS & HIS HEAD & HIS HEART IS AN ARTISAN.
• -OSMUND OF VELTARRA
• OR the below statement-
• Craftsmen that Care
Should not have
• Any additional verbiage not specified above including any type of verbiage about what kind of company we are. For instance- Integrity, reputable... It's just all played out. Im just looking for a bitching design that has the info that compliments my logo/branding.

```html
<!DOCTYPE html>
<html lang="en">
<head>
<meta charset="UTF-8">
<title>Pendrick Homeworks — Yard Sign</title>
<link href="https://fonts.googleapis.com/css2?family=Montserrat:ital,wght@0,500;0,600;0,700;1,500&display=swap" rel="stylesheet">
<style>
  :root {
    --backdrop: #9a9a9a;
    --orange-top: #f37122;
    --orange-bottom: #f78f20;
    --white: #ffffff;
    --body-top: #d9d9d9;
    --body-bottom: #ffffff;
    --brand-brown: #8b7a66;
    --mark-tone: #8a7763;
    --quote-ink: #4a3a2e;
  }
  * { margin: 0; padding: 0; box-sizing: border-box; }
  html, body { width: 1200px; height: 1000px; overflow: hidden; }
  body {
    background: var(--backdrop);
    font-family: "Montserrat", Arial, sans-serif;
    position: relative;
  }
  .sign {
    position: absolute;
    left: 268px; top: 42px;
    width: 666px; height: 886px;
    background: linear-gradient(to bottom, var(--body-top) 20%, var(--body-bottom) 80%);
    overflow: hidden;
  }
  .sign-header { position: absolute; left: 0; top: 0; width: 666px; height: 400px; }
  .header-text { position: absolute; left: 0; top: 0; width: 666px; text-align: center; color: var(--white); }
  .headline { position: absolute; left: 0; width: 100%; top: 12px; font-size: 104px; font-weight: 700; letter-spacing: -1px; line-height: 1; }
  .phone { position: absolute; left: 0; width: 100%; top: 140px; font-size: 78px; font-weight: 700; line-height: 1; letter-spacing: -1px; }
  .website { position: absolute; left: 0; width: 100%; top: 233px; font-size: 35px; font-weight: 600; line-height: 1; }
  .license { position: absolute; left: 0; width: 100%; top: 298px; font-size: 21px; font-weight: 500; line-height: 1; }
  .brand-square {
    position: absolute; left: 190px; top: 421px;
    width: 282px; height: 254px;
    background: var(--mark-tone);
  }
  .brand-name {
    position: absolute; left: 0; width: 100%; top: 695px;
    text-align: center; font-size: 40px; font-weight: 700;
    color: var(--brand-brown); letter-spacing: 1px;
  }
  .quote {
    position: absolute; left: 0; width: 100%; top: 779px;
    text-align: center; color: var(--quote-ink);
    font-size: 15px; font-weight: 500; line-height: 21px;
  }
  .quote-source {
    position: absolute; right: 32px; top: 845px;
    font-size: 15px; font-style: italic; font-weight: 500; color: var(--quote-ink);
  }
</style>
</head>
<body>
  <div class="sign">
    <svg class="sign-header" viewBox="0 0 666 400" aria-hidden="true">
      <defs>
        <linearGradient id="headerFill" x1="0" y1="0" x2="0" y2="1">
          <stop offset="0" stop-color="#f37122"/>
          <stop offset="1" stop-color="#f78f20"/>
        </linearGradient>
      </defs>
      <polygon points="0,0 666,0 666,268 333,385 0,268" fill="url(#headerFill)"/>
      <polyline points="140,336 333,392 543,314" fill="none" stroke="#ffffff" stroke-width="4"/>
      <line x1="140" y1="225" x2="526" y2="225" stroke="#ffffff" stroke-width="1.5"/>
      <line x1="140" y1="280" x2="526" y2="280" stroke="#ffffff" stroke-width="1.5"/>
    </svg>
    <div class="header-text">
      <div class="headline">FOR SALE</div>
      <div class="phone">(555) 271-4038</div>
      <div class="website">www.pendrickhomeworks.com</div>
      <div class="license">LIC NUMBER 318562</div>
    </div>

    <div class="brand-square"></div>
    <div class="brand-name">PENDRICK HOMEWORKS</div>

    <p class="quote">
      HE WHO WORKS WITH HIS HANDS IS A LABORER.<br>
      HE WHO WORKS WITH HIS HANDS &amp; HIS HEAD IS A CRAFTSMAN.<br>
      HE WHO WORKS WITH HIS HANDS &amp; HIS HEAD &amp; HIS HEART IS AN ARTISAN.
    </p>
    <p class="quote-source">-OSMUND OF VELTARRA</p>
  </div>
</body>
</html>
```